New College Graduate Resume - Creative and unique design that stands out from the rest

Need creative resume design for recent college graduate who graduated from School of Music with a concentration in music composition and production. Striving for a contemporary layout/design that allows the resume to "be unique" and "stand out" but be polished and professional. Open to integrating moderate color/graphics as part of resume design but the design can be minus those attributes as well. Attached is raw content in 7 sections (name/contact info, education, highlights of qualifications, work experience, honors/awards, and professional affiliations). While the designer has full latitude over overall design which (section headers, font type, separation/spacing, use of bullets, justification of text, etc.) please maintain current order/sequence of the 7 sections.

Industry/Entity Type

School

Requirements
Must have
• Name (Tobias Hale Whitcombe II) should be most prominent (bold/font size) compared to remainder of resume copy.
• Section headers should be prominent but less so when compared to name on resume.
• The attached file of resume content is provided as raw source copy and is NOT to be just copied and pasted into open fields as is. Expectation is each section of copy will be organized in a manner that is most visually appealing and may include bullets, appropriate spacing, etc.
Should not have
• The attached file of resume content is provided as source copy and is NOT to be just copied and pasted into open fields as is. Expectation is each section of copy will be organized in a manner that

```html
<!DOCTYPE html>
<html lang="en">
<head>
<meta charset="utf-8">
<title>Tobias Hale Whitcombe II — Resume</title>
<link rel="stylesheet" href="https://fonts.googleapis.com/css2?family=Oswald:wght@300;400;500&family=Mulish:ital,wght@0,400;0,700;0,800;1,400;1,700&display=swap">
<style>
  :root {
    --green-dark: #2f7d32;
    --green-mid: #3f9a3c;
    --green-light: #5fc25a;
    --ink: #1c1c1c;
    --muted: #555;
    --rule: #cfcfcf;
    --paper: #ffffff;
    --stage: #e4e4e4;
  }
  * { box-sizing: border-box; margin: 0; padding: 0; }
  html, body { width: 1200px; height: 690px; overflow: hidden; }
  body {
    background: var(--stage);
    font-family: "Mulish", sans-serif;
    color: var(--ink);
    position: relative;
  }
  .page {
    position: absolute;
    top: 36px;
    width: 460px;
    height: 618px;
    background: var(--paper);
    box-shadow: 0 2px 10px rgba(0,0,0,.18);
    padding: 26px 24px;
    font-size: 8px;
    line-height: 1.35;
  }
  .page--one { left: 125px; }
  .page--two { left: 615px; }

  /* Header */
  .masthead { position: relative; height: 92px; margin: 0 -24px; }
  .masthead__bar { position: absolute; top: 8px; height: 28px; background: var(--green-dark); }
  .masthead__bar--left { left: 0; width: 32px; }
  .masthead__bar--accent { left: 32px; width: 16px; background: var(--green-light); }
  .masthead__bar--right { right: 0; top: 30px; width: 148px; height: 22px; }
  .name {
    position: absolute; left: 62px; top: 0;
    font-family: "Oswald", sans-serif; line-height: .98; text-transform: uppercase;
  }
  .name__first { display: block; font-size: 36px; font-weight: 300; color: var(--green-mid); }
  .name__last { display: block; font-size: 36px; font-weight: 500; color: var(--green-dark); }

  .contact { margin: 8px 0 16px 44px; font-weight: 700; font-size: 9px; }
  .contact__row { display: flex; gap: 40px; align-items: center; }
  .contact__item { display: flex; align-items: center; gap: 5px; }
  .contact__item svg { width: 10px; height: 10px; }
  .contact__address { margin: 4px 0 0 60px; }
  .contact__label { color: var(--green-mid); }

  /* Sections */
  .section-head { display: flex; align-items: center; gap: 6px; margin-bottom: 5px; }
  .section-head__mark { width: 14px; height: 14px; background: var(--green-dark); border-radius: 2px; flex: none; }
  .section-head__title {
    font-family: "Oswald", sans-serif; font-size: 15px; font-weight: 400;
    color: var(--green-dark); text-transform: uppercase; line-height: 1;
  }
  .section-head__rule { flex: 1; height: 2px; background: var(--rule); }

  .columns { display: flex; gap: 12px; }
  .col-main { flex: 1; }
  .col-side { width: 128px; border-left: 2px solid var(--rule); padding-left: 10px; margin-top: 8px; }

  .section { margin-bottom: 12px; }
  .profile { text-align: justify; padding-right: 4px; }

  .entry { margin-bottom: 7px; }
  .entry__title { font-weight: 800; text-transform: uppercase; }
  .entry__place { font-style: italic; }
  .entry__city { font-weight: 700; font-style: italic; }

  .bullets { list-style: none; margin-top: 3px; }
  .bullets li { position: relative; padding-left: 10px; margin-bottom: 1px; }
  .bullets li::before {
    content: ""; position: absolute; left: 1px; top: 3px;
    width: 5px; height: 5px; border-radius: 50%; background: var(--green-mid);
  }
  .skills li { margin-bottom: 3px; }
  .side-title { font-size: 13px; line-height: 1.05; }

  .plain { margin-left: 10px; margin-top: 2px; }
  .affiliations { list-style: none; }
  .affiliations li { margin-bottom: 4px; }
</style>
</head>
<body>

<article class="page page--one">
  <header class="masthead">
    <span class="masthead__bar masthead__bar--left"></span>
    <span class="masthead__bar masthead__bar--accent"></span>
    <span class="masthead__bar masthead__bar--right"></span>
    <h1 class="name">
      <span class="name__first">Tobias Hale</span>
      <span class="name__last">Whitcombe II</span>
    </h1>
  </header>

  <div class="contact">
    <div class="contact__row">
      <span class="contact__item">
        <svg viewBox="0 0 10 10"><rect width="10" height="10" rx="2" fill="#3f9a3c"/><path d="M3 2.3 4.2 4 3.6 4.6c.4.8 1 1.4 1.8 1.8l.6-.6L7.7 7 7 7.8C4.8 7.6 2.4 5.2 2.2 3Z" fill="#fff"/></svg>
        555-318-2049
      </span>
      <span class="contact__item">
        <svg viewBox="0 0 10 10"><rect y="1.5" width="10" height="7" rx="1" fill="#3f9a3c"/><path d="M.5 2 5 5.5 9.5 2" fill="none" stroke="#fff" stroke-width=".9"/></svg>
        twhitcombe@mailbox.example
      </span>
    </div>
    <p class="contact__address"><span class="contact__label">ADD:</span> 82 Linden Row, Atlanta, Georgia 30300</p>
  </div>

  <div class="columns">
    <div class="col-main">
      <section class="section">
        <div class="section-head"><span class="section-head__mark"></span><h2 class="section-head__title">Profile</h2><span class="section-head__rule"></span></div>
        <p class="profile">Recent graduate of a highly ranked university seeking opportunities to apply composition and production talents across a variety of music genres and other media. Expertise lies in delivering high quality sound design, editing, mixing, and recording. Excellent interpersonal skills and the ability to build strong relationships with people at all levels. Exceptionally motivated self-starter and creative problem solver who enjoys working collaboratively on teams.</p>
      </section>

      <section class="section">
        <div class="section-head"><span class="section-head__mark"></span><h2 class="section-head__title">Education</h2><span class="section-head__rule"></span></div>
        <div class="entry">
          <p><span class="entry__title">Harbor School of Music</span> - Coastal State University</p>
          <p class="entry__place">Coral Springs, Florida</p>
        </div>
        <div class="entry">
          <p><span class="entry__title">Bachelor of Music</span> | May 2016</p>
          <p>Major: Media Writing and Production, GPA 3.20/4.0</p>
        </div>
        <div class="entry">
          <p><span class="entry__title">Maple Ridge Academy</span> | May 2011</p>
          <p>High School Diploma <strong>with Honors</strong></p>
          <p class="entry__place">College Park, Georgia</p>
        </div>
      </section>

      <section class="section">
        <div class="section-head"><span class="section-head__mark"></span><h2 class="section-head__title">Work Experience</h2><span class="section-head__rule"></span></div>
        <div class="entry">
          <p><span class="entry__title">Sound Engineer</span> | May 2014 – Present</p>
          <p>Bayline Film Studio (BFS), <span class="entry__city">Miami, FL</span></p>
          <ul class="bullets">
            <li>Edited and mixed recorded field audio to professional standards.</li>
            <li>Matched audio with motion picture video to create a seamless product.</li>
            <li>Recorded automated dialogue replacement (ADR) audio and integrated into motion picture video project using StudioDesk 11.</li>
            <li>Recorded foley sound effects to be added to film, video, and other media in post-production.</li>
            <li>Composed and recorded original music to accompany various video projects.</li>
          </ul>
        </div>
      </section>
    </div>

    <aside class="col-side">
      <div class="section-head"><span class="section-head__mark"></span><h2 class="section-head__title side-title">Highlights of Qualifications</h2></div>
      <ul class="bullets skills">
        <li>Media Production Software (StudioDesk 11)</li>
        <li>Sound Design</li>
        <li>Sound Acoustics</li>
        <li>Studio Recording</li>
        <li>Audio Editing</li>
        <li>Audio Mixing</li>
        <li>Analog/Digital board operation</li>
        <li>Music Arranging</li>
        <li>Music Composition</li>
        <li>Music Production</li>
        <li>Composing Sheet Music</li>
        <li>Singer-songwriter</li>
        <li>Rhythm guitarist</li>
      </ul>
    </aside>
  </div>
</article>

<article class="page page--two">
  <section class="section">
    <div class="section-head"><span class="section-head__mark"></span><h2 class="section-head__title">Work Experience</h2><span class="section-head__rule"></span></div>
    <div class="entry">
      <p><span class="entry__title">Sales Associate</span> | May 2013 – Oct 2013</p>
      <p>Brightmart Stores</p>
      <p>Atlanta, GA, <span class="entry__city">Atlanta, GA</span></p>
      <p class="plain">Provided customer service, maintained product displays, assisted with daily sales, and performed cashier duties during busy store hours.</p>
    </div>
    <div class="entry">
      <p><span class="entry__title">On-Site Promoter/Intern</span> | May 2012 – Aug 2012</p>
      <p>Civic Action League</p>
      <p class="plain">Promoted and advertised voter outreach events, recruited volunteers, and assisted in setting up site maps and organizing campaign materials.</p>
    </div>
    <div class="entry">
      <p><span class="entry__title">Product Marketing Consultant</span> | Jun 2011 – Aug 2011</p>
      <p>Keystone Direct, Inc.</p>
      <p class="plain">Conducted direct sales and product demonstrations for customers, presenting a compelling value proposition and building lasting client relationships.</p>
    </div>
  </section>

  <section class="section">
    <div class="section-head"><span class="section-head__mark"></span><h2 class="section-head__title">Honors/Awards</h2><span class="section-head__rule"></span></div>
    <div class="entry">
      <p class="entry__title">Evelyn R. Marsh Scholarship</p>
      <p class="entry__place">Frames and Tones 2015 Competition Winner</p>
    </div>
    <div class="entry">
      <p class="entry__title">Delta Tau Sigma Fraternity</p>
      <p>Coastal State University Homecoming Chair</p>
    </div>
  </section>

  <section class="section">
    <div class="section-head"><span class="section-head__mark"></span><h2 class="section-head__title">Professional Affiliations</h2><span class="section-head__rule"></span></div>
    <ul class="affiliations">
      <li>Member | Society of Media Composers</li>
      <li>Member | National Composers Circle</li>
      <li>Member | Sound Craft Guild</li>
      <li>Member | Delta Tau Sigma Fraternity</li>
    </ul>
  </section>
</article>

</body>
</html>
```